Trevik Builders Business Card Design Project

Clean sharp business card
Ability to write on back of card
Details for the card -
Address: PO Box 5087, Kellaway, Vic, 3614
ABN: 47 305 921 276
BSA LIC 6825170
Ph: 07 4651 2839
Fax: 07 4651 2840
Email: trevikbuilders@quillpost.net

Reason: Time to review designs after weekend

```html
<!DOCTYPE html>
<html lang="en">
<head>
<meta charset="utf-8">
<title>Trevik Builders – Business Card</title>
<link rel="stylesheet" href="https://fonts.googleapis.com/css2?family=Crimson+Pro:wght@400;700&display=swap">
<style>
  :root {
    --paper: #ffffff;
    --ink: #111111;
    --ink-soft: #1f1f1f;
    --brand-grey: #6b6c70;
    --orange: #ee7a1e;
    --divider: #ee7a1e;
  }
  html, body {
    margin: 0;
    padding: 0;
    width: 1200px;
    height: 726px;
    overflow: hidden;
    background: var(--paper);
  }
  .card {
    position: relative;
    width: 1200px;
    height: 726px;
    background: var(--paper);
    font-family: "Crimson Pro", "Palatino Linotype", Palatino, serif;
    color: var(--ink);
    overflow: hidden;
  }
  .brand-name {
    position: absolute;
    left: 72px;
    top: 118px;
    margin: 0;
    font-weight: 700;
    font-size: 50px;
    letter-spacing: 0.5px;
    line-height: 1;
    color: var(--brand-grey);
  }
  .card__rule {
    position: absolute;
    left: 72px;
    right: 72px;
    top: 420px;
    height: 4px;
    background: var(--orange);
  }
  .details {
    position: absolute;
    right: 72px;
    top: 470px;
    text-align: right;
  }
  .details__address {
    margin: 0 0 28px;
    font-weight: 700;
    font-size: 44px;
    letter-spacing: 0.3px;
    line-height: 1.1;
    color: var(--ink);
  }
  .details__line {
    margin: 0;
    font-weight: 400;
    font-size: 27px;
    line-height: 1.55;
    color: var(--ink-soft);
  }
  .details__sep {
    color: var(--divider);
    padding: 0 10px;
  }
</style>
</head>
<body>
  <main class="card">
    <h1 class="brand-name">Trevik Builders</h1>

    <div class="card__rule" aria-hidden="true"></div>

    <section class="details">
      <p class="details__address">PO Box 5087, Kellaway, Vic, 3614</p>
      <p class="details__line">ABN: 47 305 921 276<span class="details__sep">|</span>BAS LIC 6825170</p>
      <p class="details__line">T. 46512839<span class="details__sep">|</span>F. 46512840<span class="details__sep">|</span>E. trevikbuilders@quillpost.net</p>
    </section>
  </main>
</body>
</html>
```